Gaming Headset Packaging Design

We would like a gaming window box style packaging design for our gaming headset.

We want to use the packaging for 2-3 of our gaming headphone series and hence we would not like to put any product pictures on the packaging.

Size: (enclosed die-cut drawing) please feel free to modify the shape of the window
Material: E Flute Paper box
Type: Window Box style
Design features we prefer: gaming, playful, creative, trendy, High tech.
Requirement: AI file is preferred

Enclosed are a detailed description along with competitor designs and existing die-cut drawing (AI format) for your reference.

Any further questions, please feel free to ask.

```html
<!DOCTYPE html>
<html lang="en">
<head>
<meta charset="UTF-8">
<title>Pro Gaming Headset 7.1 – Window Box Dieline</title>
<link href="https://fonts.googleapis.com/css2?family=Montserrat:wght@500;600;700;800&display=swap" rel="stylesheet">
<style>
  :root {
    --paper: #ffffff;
    --board-light: #f1f2f6;
    --board-mid: #d9dce6;
    --board-dark: #b6bdd1;
    --ink-blue: #2b3192;
    --panel-blue: #24358f;
    --tri-deep: #2a3aa8;
    --tri-light: #a9c0e6;
    --cut: #8a8f9c;
    --fold: #8f95a6;
    --guide: #7fd3e0;
  }
  html, body {
    margin: 0;
    padding: 0;
    width: 1200px;
    height: 1200px;
    overflow: hidden;
    background: var(--paper);
  }
  .dieline {
    display: block;
    width: 1200px;
    height: 1200px;
    font-family: "Montserrat", sans-serif;
  }
  .panel { stroke: var(--cut); stroke-width: 1; }
  .fold { stroke: var(--fold); stroke-width: 1; stroke-dasharray: 4 3; fill: none; }
  .guide { stroke: var(--guide); stroke-width: 1; }
  .window { fill: var(--paper); stroke: var(--cut); stroke-width: 1; }
  .brand-name { fill: var(--ink-blue); font-weight: 800; font-size: 42px; letter-spacing: 0.5px; }
  .brand-sub { fill: var(--ink-blue); font-weight: 700; font-size: 19px; }
  .info-box { fill: var(--panel-blue); }
  .info-title { fill: #ffffff; font-weight: 700; font-size: 21px; }
  .info-body { fill: #ffffff; font-weight: 500; font-size: 9.6px; }
  .info-label { font-weight: 700; font-size: 11px; }
</style>
</head>
<body>
<svg class="dieline" viewBox="0 0 1500 1500" xmlns="http://www.w3.org/2000/svg">
  <defs>
    <linearGradient id="boardGrad" x1="0" y1="0" x2="1" y2="0.4">
      <stop offset="0" stop-color="var(--board-light)"/>
      <stop offset="0.6" stop-color="var(--board-mid)"/>
      <stop offset="1" stop-color="var(--board-dark)"/>
    </linearGradient>
    <linearGradient id="flapGrad" x1="0" y1="0" x2="1" y2="0">
      <stop offset="0" stop-color="#f6f7fa"/>
      <stop offset="1" stop-color="#d7dbe5"/>
    </linearGradient>
    <linearGradient id="darkFlapGrad" x1="0" y1="0" x2="1" y2="0">
      <stop offset="0" stop-color="#d2d6e2"/>
      <stop offset="1" stop-color="#b7bed2"/>
    </linearGradient>
    <linearGradient id="shardGrad" x1="0" y1="0" x2="1" y2="1">
      <stop offset="0" stop-color="var(--tri-deep)"/>
      <stop offset="0.5" stop-color="var(--tri-light)"/>
      <stop offset="1" stop-color="var(--tri-deep)"/>
    </linearGradient>
  </defs>

  <!-- registration guides -->
  <g class="guides">
    <line class="guide" x1="80" y1="210" x2="80" y2="1225"/>
    <line class="guide" x1="315" y1="210" x2="315" y2="250"/>
    <line class="guide" x1="748" y1="210" x2="748" y2="300"/>
    <line class="guide" x1="1460" y1="210" x2="1460" y2="540"/>
    <line class="guide" x1="20" y1="247" x2="315" y2="247"/>
    <line class="guide" x1="20" y1="535" x2="80" y2="535"/>
    <line class="guide" x1="20" y1="1055" x2="80" y2="1055"/>
    <line class="guide" x1="20" y1="1222" x2="80" y2="1222"/>
  </g>

  <!-- top flaps -->
  <g class="top-flaps">
    <path class="panel" fill="#ffffff" d="M85 535 L85 510 L117 405 L308 405 L308 535 Z"/>
    <path class="panel" fill="url(#flapGrad)" d="M318 535 L318 300 L314 300 L318 260 Q320 247 335 247 L730 247 Q745 247 745 262 L745 300 L748 300 L748 535 Z"/>
    <path class="fold" d="M318 300 L745 300 M340 306 L488 306 L488 300 M575 300 L575 306 L722 306"/>
    <path class="panel" fill="url(#flapGrad)" d="M755 535 L755 405 L945 405 L980 510 L980 535 Z"/>
    <path class="panel" fill="url(#darkFlapGrad)" d="M1158 578 L1158 505 Q1158 492 1172 492 L1228 492 Q1242 492 1242 505 L1242 578 Z"/>
  </g>

  <!-- main body -->
  <path class="panel" fill="url(#boardGrad)" d="M80 535 L1418 535 L1460 550 L1460 1040 L1418 1055 L80 1055 Z"/>

  <!-- decorative shard artwork areas -->
  <polygon role="img" aria-label="Abstract blue 3D triangle shard pattern" fill="url(#shardGrad)" opacity="0.55"
    points="80,540 180,580 260,690 360,660 560,770 600,830 600,1030 520,1030 420,900 260,1000 160,980 80,960"/>
  <polygon role="img" aria-label="Abstract blue 3D triangle shard pattern" fill="url(#shardGrad)" opacity="0.55"
    points="1100,810 1400,690 1460,660 1460,990 1410,1030 1240,1000 1130,1030 1100,960"/>

  <!-- fold lines -->
  <g class="folds">
    <line class="fold" x1="80" y1="535" x2="1418" y2="535"/>
    <line class="fold" x1="80" y1="1055" x2="1418" y2="1055"/>
    <line class="fold" x1="315" y1="535" x2="315" y2="1055"/>
    <line class="fold" x1="748" y1="535" x2="748" y2="1055"/>
    <line class="fold" x1="983" y1="535" x2="983" y2="1055"/>
    <line class="fold" x1="1418" y1="535" x2="1418" y2="1055"/>
    <line class="fold" x1="318" y1="535" x2="748" y2="535"/>
  </g>

  <!-- window cut-out -->
  <path class="window" d="M580 665 L655 600 L845 600 L835 608 L970 608 L985 600 L1068 600 L1113 640 L1113 1002 L960 1002 L965 985 L830 992 L840 1002 L580 1002 L580 925 L597 910 L597 800 L580 785 Z"/>

  <!-- bottom flaps -->
  <g class="bottom-flaps">
    <path class="panel" fill="#ffffff" d="M85 1055 L308 1055 L308 1060 L195 1158 L195 1215 Q195 1222 188 1222 L85 1222 Z"/>
    <path class="panel" fill="url(#flapGrad)" d="M318 1055 L745 1055 L745 1222 L655 1222 Q647 1222 647 1214 L647 1172 L417 1172 L417 1222 L318 1222 Z"/>
    <path class="panel" fill="url(#flapGrad)" d="M755 1060 L980 1060 L980 1222 L877 1222 Q868 1222 868 1214 L868 1165 Z"/>
    <path class="panel" fill="url(#darkFlapGrad)" d="M987 1060 L1415 1060 L1313 1170 L1313 1210 Q1313 1222 1300 1222 L1100 1222 Q1087 1222 1087 1210 L1087 1170 Z"/>
  </g>

  <!-- top flap branding (reads upside down on the flat sheet) -->
  <g class="brand brand-top" transform="rotate(180 527 415)">
    <text class="brand-name" x="527" y="445" text-anchor="middle">YOUR LOGO</text>
    <text class="brand-sub" x="527" y="468" text-anchor="middle">Pro Gaming Headset 7.1</text>
  </g>

  <!-- front branding -->
  <g class="brand brand-front">
    <text class="brand-name" x="459" y="597" text-anchor="middle">YOUR LOGO</text>
    <text class="brand-sub" x="460" y="620" text-anchor="middle">Pro Gaming Headset 7.1</text>
  </g>

  <!-- features -->
  <g class="features">
    <rect class="info-box" x="325" y="940" width="202" height="110"/>
    <text class="info-title" x="332" y="962">Features:</text>
    <text class="info-body" x="332" y="978">• Virtual 7.1 Surround Sound</text>
    <text class="info-body" x="332" y="993">• Dual Drivers on each ear for Accuracy</text>
    <text class="info-body" x="332" y="1008">• 3D Sound Vibration</text>
    <text class="info-body" x="332" y="1024">• Bendable Stainless-Steel headband</text>
    <text class="info-body" x="332" y="1039">• Soft and soothing earpads</text>
  </g>

  <!-- specification -->
  <g class="specification">
    <rect class="info-box" x="1128" y="603" width="274" height="342"/>
    <text class="info-title" x="1137" y="628">Specification:</text>
    <text class="info-body" x="1137" y="644">Headphone Specification Speaker Diameter: Q40mm</text>
    <text class="info-body" x="1137" y="659">Impedance: 32Q + 15 Sensitivity S.P.L: 113dB + 3dB</text>
    <text class="info-body" x="1137" y="675">Rated Power: 20mW Aggregate capability: 30mW</text>
    <text class="info-body" x="1137" y="690">Frequency Response: 20-20kHz Plug Type: 3.5mm</text>
    <text class="info-body" x="1137" y="705">Stereo Microphone Specification Microphone Unit: Q6</text>
    <text class="info-body" x="1137" y="721">x 5mm Sensitivity S.P.L 34dB + 3dB Impedance: &lt;2.2k</text>
    <text class="info-body" x="1137" y="736">Frequency Response: 30-16kHz Standard Operating</text>
    <text class="info-body" x="1137" y="751">Voltage: 4.5V S/N Ratio: Z 60dB Plug Type: 3.5mm</text>
    <text class="info-body" x="1137" y="767">Stereo</text>

    <text class="info-body" x="1137" y="801"><tspan class="info-label">Warning:</tspan> Adjust headphone's sound to a proper</text>
    <text class="info-body" x="1137" y="817">volume. Loud sound may damage your ears. For traffic</text>
    <text class="info-body" x="1137" y="832">safety never use the headset while driving.</text>

    <text class="info-body" x="1137" y="870"><tspan class="info-label">Caution:</tspan> If the user attempts to inspect or modify</text>
    <text class="info-body" x="1137" y="886">the product in any way we don't guarantee the</text>
    <text class="info-body" x="1137" y="901">performance of the product. Specifications and design</text>
    <text class="info-body" x="1137" y="916">are subject to possible modification notice due to</text>
    <text class="info-body" x="1137" y="932">improvements.</text>
  </g>
</svg>
</body>
</html>
```